Good Morning Banner

We need a banner design (20.4 x 10.14) with the words 'Good Morning' as the main feature and the words 'Pastor R.K. Adeyemi-Lowe' underneath. Attached is an example but let your creative juices flow!

Target Market(s)

Christian

```html
<!DOCTYPE html>
<html lang="en">
<head>
<meta charset="utf-8">
<title>Good Morning Banner</title>
<link href="https://fonts.googleapis.com/css2?family=Barlow+Condensed:wght@500;600;700&display=swap" rel="stylesheet">
<style>
  :root {
    --sun-yellow: #ffe11a;
    --white: #ffffff;
    --bar: rgba(18, 22, 26, 0.82);
    --leaf-deep: #2f5a1e;
    --leaf: #6f9a3a;
    --leaf-light: #b9d58a;
    --sky-blue: #3f8fd0;
    --lilac: #c3c6e6;
  }
  html, body {
    margin: 0;
    padding: 0;
    overflow: hidden;
    background: #1a1f24;
  }
  .banner {
    position: relative;
    width: 1200px;
    height: 597px;
    overflow: hidden;
    font-family: "Barlow Condensed", "Arial Narrow", sans-serif;
  }
  .banner__photo {
    position: absolute;
    inset: 0;
    background:
      radial-gradient(circle at 82% 35%, var(--lilac) 0%, rgba(195,198,230,0) 30%),
      radial-gradient(ellipse at 50% 80%, var(--sky-blue) 0%, rgba(63,143,208,0) 35%),
      radial-gradient(circle at 20% 30%, var(--leaf-light) 0%, rgba(185,213,138,0) 35%),
      linear-gradient(120deg, var(--leaf-deep) 0%, var(--leaf) 45%, #8fb86a 70%, #a9c4b8 100%);
  }
  .headline {
    position: absolute;
    right: 44px;
    top: 330px;
    margin: 0;
    font-weight: 700;
    font-size: 141px;
    line-height: 1;
    letter-spacing: 1px;
    text-transform: uppercase;
    white-space: nowrap;
  }
  .headline__good { color: var(--sun-yellow); }
  .headline__morning { color: var(--white); margin-left: 26px; }
  .speaker {
    position: absolute;
    right: 47px;
    top: 462px;
    margin: 0;
    color: var(--white);
    font-weight: 600;
    font-size: 22px;
    line-height: 1;
    letter-spacing: 2px;
    text-transform: uppercase;
    white-space: nowrap;
  }
  .info-bar {
    position: absolute;
    left: 0;
    right: 0;
    bottom: 0;
    height: 56px;
    background: var(--bar);
    display: flex;
    align-items: center;
    color: var(--sun-yellow);
    font-weight: 600;
    font-size: 25px;
    letter-spacing: 2px;
  }
  .info-bar__channel { position: absolute; left: 54px; }
  .info-bar__web { position: absolute; left: 650px; display: flex; align-items: center; gap: 16px; }
  .info-bar__social { position: absolute; left: 958px; display: flex; align-items: center; gap: 14px; }
  .icon { width: 34px; height: 34px; display: block; }
  .social-dot {
    width: 30px;
    height: 30px;
    border: 2px solid var(--white);
    border-radius: 50%;
    box-sizing: border-box;
  }
</style>
</head>
<body>
  <div class="banner">
    <div class="banner__photo" role="img" aria-label="Two smiling men in sunglasses greeting each other outdoors among sunlit green trees and flowers"></div>

    <h1 class="headline"><span class="headline__good">Good</span><span class="headline__morning">Morning</span></h1>
    <p class="speaker">Pastor R.K. Adeyemi-Lowe</p>

    <div class="info-bar">
      <span class="info-bar__channel">dawnlight.tv</span>
      <span class="info-bar__web">
        <svg class="icon" viewBox="0 0 34 34" fill="none" stroke="#ffffff" stroke-width="2">
          <circle cx="17" cy="17" r="15"/>
          <ellipse cx="17" cy="17" rx="6.5" ry="15"/>
          <line x1="2" y1="17" x2="32" y2="17"/>
          <path d="M5 9.5h24M5 24.5h24"/>
          <line x1="17" y1="2" x2="17" y2="32"/>
        </svg>
        www.dawnlight.tv
      </span>
      <span class="info-bar__social">
        <span class="social-dot"></span>
        rkaministries
      </span>
    </div>
  </div>
</body>
</html>
```